CopperWanderer Stretching and Strength

We need a application design for a our first IOS application. the goal of the application is to categorize stretching and strength routines for triathlon.

We would like to see designs that use the color orange.

The design of the application should be compliant with the last version of the IOS Mobile.

For this first design we need the folowing pages:

1- Sign up
2- Log in
3- Home
4- View Exercises
5- Do it
6- Profile

The description of each page is in the attached document.

We need a logo design for the application. The logo should express that mission of the application that is for stretch and strength training for Triathlon.

We will use https://zelvanstack.example to develop the application, if you have any experience of the limitation that this technology have it will be a plus.

If you have any question please feel free to contact us.
Updates

Project Deadline Extended
Reason: We will extend the deadline to be sure that we select the best design from all of you. we will take the final decision next Tuesday.

Target Market(s)

The market for my aplicación is the Running a Triathlon world.

Logo Text

CopperWanderer

Font styles to use
Serif

Colors
f37122
ffffff
dcdcdc

Requirements
Must have
• In some future we will add more features in the menu. We should considere it for the design.
• The designs should include all the screens in the power point.

```html
<!DOCTYPE html>
<html lang="en">
<head>
<meta charset="utf-8">
<title>CopperWanderer — Navigation Drawer</title>
<link rel="stylesheet" href="https://fonts.googleapis.com/css2?family=Roboto:wght@400;500&display=swap">
<style>
  :root {
    --orange: #f37122;
    --white: #ffffff;
    --grey-line: #dcdcdc;
    --canvas: #d6e3ef;
    --page: #f2f2f2;
    --ink: #3a3a3a;
    --ink-soft: #777777;
    --footer: #eeeeee;
  }
  * { box-sizing: border-box; margin: 0; padding: 0; }
  html, body {
    width: 1200px; height: 1200px; overflow: hidden;
    background: var(--canvas);
    font-family: "Roboto", Arial, sans-serif;
  }
  .screen {
    position: absolute; left: 270px; top: 12px;
    width: 660px; height: 1176px;
    background: var(--page); overflow: hidden;
  }
  .status-bar {
    position: absolute; left: 0; top: 0; width: 660px; height: 46px;
    background: var(--orange); color: var(--white);
    font-size: 19px;
  }
  .status-bar span { position: absolute; top: 12px; }
  .app-bar {
    position: absolute; left: 516px; top: 46px; width: 144px; height: 72px;
    background: var(--orange);
  }
  .menu-icon { position: absolute; left: 14px; top: 24px; }

  .card {
    position: absolute; left: 532px; width: 140px;
    background: var(--white); box-shadow: 0 1px 3px rgba(0,0,0,.12);
    overflow: hidden;
  }
  .chart-card { top: 139px; height: 351px; }
  .history-card { top: 505px; height: 463px; }
  .sponsor-card { top: 983px; height: 176px; }
  .card-title { position: absolute; left: 27px; font-size: 22px; color: var(--ink); }
  .today { position: absolute; left: 88px; top: 18px; font-size: 18px; color: var(--orange); }
  .axis-label {
    position: absolute; left: 26px; top: 196px; font-size: 15px; color: var(--ink-soft);
    transform: rotate(-90deg); transform-origin: left top; white-space: nowrap;
  }
  .axis-y { position: absolute; left: 67px; top: 102px; width: 1px; height: 201px; background: var(--grey-line); }
  .axis-x { position: absolute; left: 67px; top: 302px; width: 80px; height: 1px; background: var(--grey-line); }
  .bar { position: absolute; left: 120px; top: 211px; width: 10px; height: 92px; background: var(--orange); }
  .bar-label { position: absolute; left: 100px; top: 184px; font-size: 15px; color: var(--ink-soft); }
  .tick-label { position: absolute; left: 46px; top: 312px; font-size: 15px; color: var(--ink-soft); }
  .pager {
    position: absolute; left: -14px; top: 150px; width: 52px; height: 52px; border-radius: 50%;
    background: #e2e2e2;
  }
  .history-photo { position: absolute; left: 27px; width: 100px; }
  .divider { position: absolute; left: 0; width: 140px; height: 1px; background: var(--grey-line); }
  .sponsor-tile {
    position: absolute; left: 19px; top: 62px; width: 130px; height: 99px;
    border: 1px solid var(--grey-line);
  }
  .sponsor-name { position: absolute; left: 22px; top: 36px; font-size: 24px; font-weight: 500; color: #111; white-space: nowrap; }

  .drawer {
    position: absolute; left: 0; top: 46px; width: 516px; height: 1130px;
    background: var(--white); box-shadow: 3px 0 8px rgba(0,0,0,.18);
  }
  .avatar { position: absolute; left: 15px; top: 33px; width: 118px; height: 118px; border-radius: 50%;
    background: radial-gradient(circle at 50% 45%, #c58f6d 0 32%, #4d5a3a 60%, #6f7f55 100%); }
  .user-name { position: absolute; left: 155px; top: 54px; font-size: 26px; font-weight: 500; color: var(--ink); }
  .user-email { position: absolute; left: 155px; top: 94px; font-size: 21px; color: var(--orange); }
  .edit-btn { position: absolute; left: 470px; top: 86px; width: 34px; height: 34px; border-radius: 50%; background: var(--orange); }

  .nav-item { position: absolute; left: 84px; font-size: 22px; font-weight: 500; color: var(--ink); }
  .nav-item.active { color: var(--orange); }
  .nav-sub { position: absolute; left: 84px; font-size: 21px; color: var(--ink-soft); }
  .nav-icon { position: absolute; left: 18px; }

  .version {
    position: absolute; left: 0; bottom: 0; width: 516px; height: 54px;
    background: var(--footer); font-size: 18px; color: var(--ink);
    text-align: center; line-height: 54px;
  }
</style>
</head>
<body>
<main class="screen">
  <div class="status-bar">
    <span style="left:10px">●●●○○ NORTHCELL</span>
    <span style="left:292px">4:21 PM</span>
    <span style="left:556px">100%</span>
    <svg style="position:absolute;left:610px;top:16px" width="40" height="16" viewBox="0 0 40 16"><rect x="1" y="1" width="34" height="14" rx="3" fill="none" stroke="#fff" stroke-width="1.5"/><rect x="3" y="3" width="30" height="10" rx="1.5" fill="#fff"/><rect x="36" y="5" width="3" height="6" fill="#fff"/></svg>
  </div>
  <div class="app-bar">
    <svg class="menu-icon" width="30" height="20" viewBox="0 0 30 20"><g fill="#fff"><rect y="0" width="30" height="3"/><rect y="8" width="30" height="3"/><rect y="16" width="30" height="3"/></g></svg>
  </div>

  <section class="card chart-card">
    <div class="pager"></div>
    <span class="today">Today</span>
    <span class="axis-label">Lorem ipsum</span>
    <div class="axis-y"></div><div class="axis-x"></div>
    <span class="bar-label">Lorem</span>
    <div class="bar"></div>
    <span class="tick-label">10am</span>
  </section>

  <section class="card history-card">
    <span class="card-title" style="top:18px">History</span>
    <div class="history-photo" role="img" aria-label="Group doing outdoor stretching in a park" style="top:94px;height:90px;background:linear-gradient(160deg,#a9b9a0,#5f7452 60%,#3f4a39)"></div>
    <div class="divider" style="top:244px"></div>
    <div class="history-photo" role="img" aria-label="Class doing floor stretches in a studio" style="top:264px;height:90px;background:linear-gradient(160deg,#c9a79a,#7a4a4a 55%,#a8643a)"></div>
    <div class="divider" style="top:414px"></div>
    <div class="history-photo" role="img" aria-label="Workout photo" style="top:435px;height:28px;background:linear-gradient(90deg,#d8d0cc,#8a7d78)"></div>
  </section>

  <section class="card sponsor-card">
    <span class="card-title" style="top:16px">Sponsors</span>
    <div class="sponsor-tile"><span class="sponsor-name">Stridemark</span></div>
  </section>

  <nav class="drawer">
    <div class="avatar" role="img" aria-label="User profile photo"></div>
    <div class="user-name">Dara Okonkwo</div>
    <div class="user-email">dara.okonkwo@mailbox.example</div>
    <div class="edit-btn">
      <svg width="34" height="34" viewBox="0 0 34 34"><path d="M11 23 L12 19 L21 10 L24 13 L15 22 Z" fill="#fff"/></svg>
    </div>

    <svg class="nav-icon" style="top:230px" width="24" height="26" viewBox="0 0 24 26"><circle cx="12" cy="7" r="6" fill="#666"/><path d="M3 25 Q3 14 12 14 Q21 14 21 25 Z" fill="#666"/></svg>
    <span class="nav-item" style="top:232px">Profile</span>

    <svg class="nav-icon" style="top:300px" width="28" height="24" viewBox="0 0 28 24"><path d="M14 1 L27 12 L23 12 L23 23 L17 23 L17 16 L11 16 L11 23 L5 23 L5 12 L1 12 Z" fill="var(--orange)"/></svg>
    <span class="nav-item active" style="top:301px">Home</span>

    <svg class="nav-icon" style="top:368px" width="26" height="26" viewBox="0 0 26 26"><circle cx="6" cy="14" r="3" fill="#666"/><path d="M20 2 L22 24 L18 24 L17 14 L9 16 L9 12 Z" fill="#666"/></svg>
    <span class="nav-item" style="top:370px">Stretching</span>
    <span class="nav-sub" style="top:440px">View Stretch</span>
    <span class="nav-sub" style="top:508px">View Routines</span>

    <svg class="nav-icon" style="top:576px" width="26" height="26" viewBox="0 0 26 26"><path d="M3 20 Q4 24 14 23 Q24 22 24 15 Q22 10 16 13 L15 6 L10 3 L10 7 L12 8 L11 15 Q6 15 3 20 Z" fill="#666"/></svg>
    <span class="nav-item" style="top:578px">Strength</span>
    <span class="nav-sub" style="top:648px">View Exercises</span>
    <span class="nav-sub" style="top:716px">View Routines</span>

    <svg class="nav-icon" style="top:784px" width="28" height="26" viewBox="0 0 28 26"><path d="M2 2 L16 2 L16 24 L2 24 Z M5 4 L5 22 L11 20 L11 6 Z" fill="#666" fill-rule="evenodd"/><path d="M17 11 L22 11 L22 7 L27 13 L22 19 L22 15 L17 15 Z" fill="#666"/></svg>
    <span class="nav-item" style="top:786px">Log Out</span>

    <div class="version">Version 0.0.1</div>
  </nav>
</main>
</body>
</html>
```